Sprout & Soar General Card Design

Please see http://sprout-and-soar.example.org for more information about our program. In brief, we are a 501(c)(3) nonprofit organization that focuses on improving educational outcomes for all students through parent education and empowerment, K-12 curriculum development, K-12 staff development, learner-oriented live events, community service projects, and more. We are now preparing to launch our Sprout & Soar Educational Series, which is devoted to teaching children and the adults in their lives about making healthy food choices and regaining control over what is in their food by growing it themselves in easy, affordable self-watering container gardens that can be placed in spaces not otherwise suitable for growing fruits and vegetables, such as paved lots and rooftops, are portable, and can be quickly built from recycled materials. In fact, we have local businesses already lining up to donate clean, safe 5-gallon buckets for this initiative (our container design uses 5-gallon buckets). We have already built out content on the site to support as many of the Trail Rover merit badges as we could tie to the instructional goals of our Sprout & Soar Educational Series. We are in the processes of developing K-12 curricula tied to the Common Core and STEM (science, technology, engineering, & math), which we will be giving away for free under a Creative Commons license to help public schools in states that have recently adopted the Common Core but can't afford to replace all their textbooks and don't have the time to scramble to create curricula of their own. This card will be used by all of our Sprout & Soar staff and volunteers to share out information about the program and promote it to others. It will go out in mailings, sit on display tables at events, be left at kiosks, and be handed out in person. It needs to be color-matched to our Sprout & Soar site. The logo on the site we created for our Sprout & Soar Educational Series was done using an online service and the quality of the image is quite poor (see attached file). When we use it in print materials and then convert them to PDF, the logo becomes pixelated. It's awful. We are not entirely married to keeping the logo if you can come up with something better and we are given the final JPG or PNG file of the logo to upload to the site so they match. If you can just improve the quality of the existing logo, that's fine, too. Please note that the phrase "Sprout & Soar Educational Series" is a service mark of BrightHome4Kids and should be followed by the letters "SM" in superscript at the end of the word "Series" in any logo you create.
Target Market(s)
parents of K-12 students, K-12 teachers, community service organizations, youth organizations, programs for the elderly, programs for the disabled
Industry/Entity Type
Community Service
Contact Information for Business Card
BrightHome4Kids' Sprout & Soar Educational Series, http://sprout-and-soar.example.org, (555) 214-7389, Non-GMO/Organic Family & Community Gardening Workshops, K-12 Common Core/STEM Curricula Development, Community Service Projects, Online Gardening & Teaching Communities, Project-Based Learning Activities, Youth Leadership Projects, Fun Contests and Prizes, Corporate & Small Business Social Responsibility Programs, K-12 Staff Development, Education Research & Reporting

```html
<!DOCTYPE html>
<html lang="en">
<head>
<meta charset="utf-8">
<title>Sprout &amp; Soar – General Card</title>
<link rel="stylesheet" href="https://fonts.googleapis.com/css2?family=Arimo:ital,wght@0,400;0,700;1,400&display=swap">
<style>
  :root {
    --khaki-top: #c9cbaa;
    --olive-bottom: #8e9470;
    --panel-black: #050505;
    --bar-dark: #3a3a3a;
    --bar-light: #7a7a7a;
    --text-white: #ffffff;
    --accent-orange: #f2ab3c;
    --soil-warm: #6a4a36;
    --leaf-green: #4f6e3a;
  }
  * { box-sizing: border-box; margin: 0; padding: 0; }
  html, body {
    width: 1200px; height: 702px; overflow: hidden;
    background: var(--khaki-top);
  }
  .card {
    position: relative; width: 1200px; height: 702px;
    font-family: "Arimo", Arial, sans-serif;
    color: var(--text-white);
    background: var(--khaki-top);
  }
  .top-band { position: absolute; left: 0; top: 0; width: 1200px; height: 46px; background: var(--khaki-top); }
  .feature-panel { position: absolute; left: 0; top: 46px; width: 1200px; height: 490px; background: var(--panel-black); overflow: hidden; }
  .hands-photo {
    position: absolute; left: 380px; top: 0; width: 520px; height: 490px;
    background:
      radial-gradient(ellipse 90px 150px at 52% 38%, rgba(79,110,58,0.75), rgba(79,110,58,0) 100%),
      radial-gradient(ellipse 240px 170px at 50% 72%, rgba(106,74,54,0.9), rgba(106,74,54,0) 100%),
      radial-gradient(ellipse 300px 230px at 50% 60%, rgba(140,100,80,0.45), rgba(0,0,0,0) 100%);
  }
  .service-list { position: absolute; list-style: none; font-size: 31px; line-height: 37px; }
  .service-list li { position: absolute; left: 0; white-space: nowrap; padding-left: 20px; }
  .service-list li::before { content: "•"; position: absolute; left: 0; }
  .service-list--left { left: 64px; top: 0; }
  .service-list--right { left: 652px; top: 0; }
  .nonprofit-note {
    position: absolute; left: 704px; top: 399px;
    font-size: 30px; line-height: 35px; font-style: italic;
    color: var(--accent-orange);
  }
  .share-bar {
    position: absolute; left: 0; top: 536px; width: 1200px; height: 89px;
    background: linear-gradient(90deg, var(--bar-dark) 0%, #4a4a4a 50%, var(--bar-light) 100%);
  }
  .share-icons { position: absolute; left: 58px; top: 33px; display: flex; gap: 7px; }
  .share-icon { width: 37px; height: 37px; border-radius: 7px; }
  .site-url {
    position: absolute; right: 40px; top: 30px;
    font-size: 31px; font-weight: 700; line-height: 40px;
    white-space: nowrap; color: var(--text-white);
  }
  .bottom-band { position: absolute; left: 0; top: 625px; width: 1200px; height: 77px; background: var(--olive-bottom); }
</style>
</head>
<body>
<div class="card">
  <div class="top-band"></div>

  <section class="feature-panel">
    <div class="hands-photo" role="img" aria-label="Photo of cupped hands holding soil with a young green seedling"></div>

    <ul class="service-list service-list--left">
      <li style="top:66px">Non-GMO/Organic Family and<br>Community Gardening Workshops</li>
      <li style="top:161px">K-12 Common Core/STEM<br>Curricula Development</li>
      <li style="top:259px">Community Service Projects</li>
      <li style="top:317px">Online Gardening and<br>Teaching Communities</li>
      <li style="top:417px">Project-Based Learning Activities</li>
    </ul>

    <ul class="service-list service-list--right">
      <li style="top:64px">Youth Leadership Projects</li>
      <li style="top:123px">Fun Contests and Prizes</li>
      <li style="top:182px">Corporate &amp; Small Business<br>Social Responsibility Programs</li>
      <li style="top:278px">K-12 Staff Development</li>
      <li style="top:337px">Education Research and Reporting</li>
    </ul>

    <p class="nonprofit-note">BrightHome4Kids is a 501(c)(3)<br>non-profit organization.</p>
  </section>

  <section class="share-bar">
    <div class="share-icons" aria-label="Social sharing links">
      <span class="share-icon" style="background:#4a6190"></span>
      <span class="share-icon" style="background:#3a9fcf"></span>
      <span class="share-icon" style="background:#3e7fa6"></span>
      <span class="share-icon" style="background:#c8454f"></span>
      <span class="share-icon" style="background:#e06a2c"></span>
      <span class="share-icon" style="background:#4d6580"></span>
      <span class="share-icon" style="background:#5a5a55"></span>
      <span class="share-icon" style="background:#c9c4be"></span>
      <span class="share-icon" style="background:#3a5f80"></span>
      <span class="share-icon" style="background:#8f8f8f"></span>
      <span class="share-icon" style="background:#b6794a"></span>
      <span class="share-icon" style="background:#5c8c50"></span>
    </div>
    <div class="site-url">www.sprout-and-soar.example.org</div>
  </section>

  <div class="bottom-band"></div>
</div>
</body>
</html>
```